Christmas Postcard a manufacturer of skirting boards

Relaunch of the Christmas greetings Postcard of a company manufacturing premium quality skirting boards from real wood. Please refer to http://www.brumholt-profile.example/

- Christmas greetings Postcard 105 mm x 210 mm (card will be sent without envelope)

frontside:
- your graphic design, including
- Logo on the card
- Greetings "Frohe Weihnachten und ein erfolgreiches neues Jahr" on the card (front)
- insert Wooden Earring(s) - for recognition!

backside: (on the left)
"Wir bedanken uns für die partnerschaftliche Zusammenarbeit und freuen uns darauf, Sie auch im Jahr 2016 mit unseren Angeboten, Ideen und Know-how bei der Verwirklichung Ihrer Vorhaben zu unterstützen. (see pdf´s)

Ihnen und Ihren Mitarbeitern wünschen wir ein zauberhaftes Weihnachtsfest und für das neue Jahr Gesundheit, Glück, Erfolg und Freude."

Signatures (see pdf`s)

backside (on the right):
Adress field

------
The pdf´s from last years are just for the color mood. Fresh, modern design appreciated, no comic style.

Industry/Entity Type

It Company

Requirements
Must have
• "Wooden Earring(s)"

```html
<!DOCTYPE html>
<html lang="de">
<head>
<meta charset="utf-8">
<title>Weihnachtspostkarte Brumholt</title>
<link href="https://fonts.googleapis.com/css2?family=Great+Vibes&family=Cormorant+Garamond:wght@500&family=Open+Sans:wght@400;600&display=swap" rel="stylesheet">
<style>
  :root {
    --stage: #e6e6e6;
    --paper: #ffffff;
    --wood-dark: #4a2a17;
    --wood-mid: #8a5a34;
    --wood-light: #c79a66;
    --snow: #f4f1ec;
    --band: #5a3521;
    --band-text: #f1e4d4;
    --greeting-red: #8f1c14;
    --greeting-brown: #5b3a25;
    --ink: #333333;
    --line: #9a9a9a;
  }
  html, body {
    margin: 0;
    width: 900px;
    height: 1200px;
    overflow: hidden;
    background: var(--stage);
  }
  .card {
    position: absolute;
    left: 36px;
    width: 828px;
    background: var(--paper);
    box-shadow: 0 2px 6px rgba(0,0,0,.18);
  }
  .card--front { top: 150px; height: 435px; overflow: hidden; }
  .card--back { top: 600px; height: 420px; }

  .front-photo {
    position: absolute;
    inset: 0 0 55px 0;
    background:
      radial-gradient(ellipse at 78% 55%, var(--snow) 0%, rgba(244,241,236,.85) 35%, rgba(244,241,236,0) 62%),
      linear-gradient(100deg, var(--wood-dark) 0%, var(--wood-mid) 25%, var(--wood-light) 45%, #e8d7c0 62%, var(--snow) 80%);
  }
  .greeting {
    position: absolute;
    left: 470px;
    top: 105px;
    width: 340px;
    text-align: center;
  }
  .greeting__script {
    font-family: 'Great Vibes', cursive;
    font-size: 48px;
    color: var(--greeting-red);
    line-height: 1;
  }
  .greeting__small {
    font-family: 'Great Vibes', cursive;
    font-size: 22px;
    color: var(--greeting-brown);
    margin-top: 2px;
  }
  .greeting__year {
    font-family: 'Cormorant Garamond', serif;
    font-weight: 500;
    font-size: 50px;
    color: var(--greeting-brown);
    line-height: 1.05;
  }
  .front-band {
    position: absolute;
    left: 0; right: 0; bottom: 0;
    height: 55px;
    background: var(--band);
    display: flex;
    align-items: center;
    justify-content: space-between;
    padding: 0 30px;
    box-sizing: border-box;
  }
  .front-band__slogan {
    font-family: 'Open Sans', sans-serif;
    font-size: 15px;
    color: var(--band-text);
  }
  .brand {
    display: flex;
    align-items: center;
    gap: 10px;
  }
  .brand__mark {
    width: 14px;
    height: 14px;
    border-radius: 50%;
    background: var(--band-text);
  }
  .brand__name {
    font-family: 'Open Sans', sans-serif;
    font-weight: 400;
    font-size: 22px;
    color: var(--band-text);
    line-height: 1;
  }

  .message {
    position: absolute;
    left: 30px;
    top: 45px;
    width: 400px;
    font-family: 'Open Sans', sans-serif;
    font-size: 13.5px;
    line-height: 1.5;
    color: var(--ink);
  }
  .message p { margin: 0 0 14px; }
  .signatures {
    position: absolute;
    left: 30px;
    top: 232px;
    width: 400px;
    display: flex;
    justify-content: space-between;
  }
  .signature { width: 110px; text-align: center; }
  .signature__hand { width: 110px; height: 34px; background: linear-gradient(180deg, rgba(40,40,40,0), rgba(40,40,40,.12)); }
  .signature__name {
    font-family: 'Open Sans', sans-serif;
    font-size: 8px;
    color: #777;
    border-top: 1px solid #ccc;
    padding-top: 3px;
  }
  .stamp {
    position: absolute;
    left: 729px;
    top: 36px;
    width: 81px;
    height: 84px;
    border: 1px solid var(--line);
  }
  .address-lines {
    position: absolute;
    left: 504px;
    top: 95px;
    width: 300px;
  }
  .address-lines span {
    display: block;
    height: 44px;
    border-bottom: 1px solid var(--line);
  }
</style>
</head>
<body>
  <section class="card card--front">
    <div class="front-photo" role="img" aria-label="Foto von gestaffelten Echtholz-Sockelleisten mit eingefrästem Tannenbaum, Holzohrringen, Weihnachtsschmuck und Schneestaub"></div>
    <div class="greeting">
      <div class="greeting__script">Frohe Weihnachten</div>
      <div class="greeting__small">und ein erfolgreiches</div>
      <div class="greeting__year">Neues Jahr</div>
    </div>
    <div class="front-band">
      <span class="front-band__slogan">natürlich schön. natürlich individuell</span>
      <div class="brand">
        <span class="brand__mark"></span>
        <span class="brand__name">Brumholt</span>
      </div>
    </div>
  </section>

  <section class="card card--back">
    <div class="message">
      <p>“Wir bedanken uns für die partnerschaftliche Zusammenarbeit und freuen uns darauf, Sie auch im Jahr 2016 mit unseren Angeboten, Ideen und Know-how bei der Verwirklichung Ihrer Vorhaben zu unterstützen.</p>
      <p>Ihnen und Ihren Mitarbeitern wünschen wir ein zauberhaftes Weihnachtsfest und für das neue Jahr Gesundheit, Glück, Erfolg und Freude.”</p>
    </div>
    <div class="signatures">
      <div class="signature">
        <div class="signature__hand" role="img" aria-label="Unterschrift"></div>
        <div class="signature__name">Ingo Brumholt</div>
      </div>
      <div class="signature">
        <div class="signature__hand" role="img" aria-label="Unterschrift"></div>
        <div class="signature__name">Margit Brumholt</div>
      </div>
      <div class="signature">
        <div class="signature__hand" role="img" aria-label="Unterschrift"></div>
        <div class="signature__name">Peter Lindner</div>
      </div>
    </div>
    <div class="stamp"></div>
    <div class="address-lines"><span></span><span></span><span></span><span></span></div>
  </section>
</body>
</html>
```